Stonebay Towing Business Card

Towing
Accident towing
Mechanical breakdown
Insurance, salvage and recovery
4wd off road towing
Light & Heavy towing
8347 2516
24 hour business 7 days

Logo can be whole size on front

Industry/Entity Type

Towing/ transport

Contact Information for Business Card

The above

```html
<!DOCTYPE html>
<html lang="en">
<head>
<meta charset="utf-8">
<title>Stonebay Towing Business Card</title>
<link href="https://fonts.googleapis.com/css2?family=Oswald:wght@500;600&family=Yellowtail&family=Montserrat:wght@500&display=swap" rel="stylesheet">
<style>
  :root {
    --stage: #3a3a3a;
    --ink: #1c1c1c;
    --card-black: #222222;
    --red: #d31f26;
    --white: #ffffff;
  }
  * { margin: 0; padding: 0; box-sizing: border-box; }
  html, body { width: 1200px; height: 689px; overflow: hidden; background: var(--stage); }
  .canvas { position: relative; width: 1200px; height: 689px; }
  .card {
    position: absolute; top: 190px; width: 540px; height: 310px;
    border-radius: 22px; overflow: hidden;
  }
  .card-front { left: 45px; background: var(--card-black); display: flex; align-items: center; justify-content: center; }
  .front-brand {
    font-family: "Oswald", sans-serif; font-weight: 600; font-size: 66px;
    color: var(--red); letter-spacing: 1px; text-transform: uppercase;
    display: flex; align-items: center; gap: 16px;
  }
  .brand-dot { width: 22px; height: 22px; border-radius: 50%; background: var(--red); }
  .card-back { left: 615px; background: var(--white); }
  .back-shape { position: absolute; inset: 0; }
  .back-brand {
    position: absolute; left: 26px; top: 78px;
    font-family: "Oswald", sans-serif; font-weight: 600; font-size: 32px;
    color: var(--red); text-transform: uppercase; letter-spacing: .5px;
  }
  .contact { position: absolute; right: 26px; top: 22px; text-align: left; width: 230px; }
  .contact-name { font-family: "Yellowtail", cursive; font-size: 40px; color: var(--ink); line-height: 1; }
  .contact-phone {
    font-family: "Oswald", sans-serif; font-weight: 600; font-size: 40px; color: var(--red);
    display: flex; align-items: center; gap: 8px; line-height: 1.1;
  }
  .contact-phone svg { width: 24px; height: 24px; }
  .hours-pill {
    margin-top: 6px; display: inline-block; background: var(--ink); color: var(--white);
    font-family: "Montserrat", sans-serif; font-weight: 500; font-size: 11px; letter-spacing: 1.5px;
    padding: 5px 14px; border-radius: 14px; text-transform: uppercase;
  }
  .services-title {
    position: absolute; left: 30px; top: 176px;
    font-family: "Yellowtail", cursive; font-size: 38px; color: var(--white);
  }
  .service-list {
    position: absolute; list-style: none;
    font-family: "Oswald", sans-serif; font-weight: 500; font-size: 15px;
    color: var(--white); text-transform: uppercase; letter-spacing: .5px;
  }
  .service-list li { display: flex; align-items: center; gap: 8px; height: 23px; }
  .service-list svg { width: 16px; height: 16px; flex: none; }
  .list-left { left: 36px; top: 228px; }
  .list-right { left: 290px; top: 142px; }
</style>
</head>
<body>
<main class="canvas">
  <section class="card card-front">
    <div class="front-brand"><span class="brand-dot"></span>Stonebay Towing</div>
  </section>

  <section class="card card-back">
    <svg class="back-shape" viewBox="0 0 540 310" preserveAspectRatio="none">
      <path d="M0 180 L200 180 Q240 180 250 150 Q258 125 290 125 L540 125 L540 310 L0 310 Z" fill="var(--red)"/>
      <path d="M290 112 L540 112" stroke="var(--ink)" stroke-width="5"/>
    </svg>

    <div class="back-brand">Stonebay Towing</div>

    <div class="contact">
      <div class="contact-name">Liam Carter</div>
      <div class="contact-phone">
        <svg viewBox="0 0 24 24"><path d="M6.6 10.8a15 15 0 0 0 6.6 6.6l2.2-2.2a1 1 0 0 1 1-.25 11.4 11.4 0 0 0 3.6.57 1 1 0 0 1 1 1V20a1 1 0 0 1-1 1A17 17 0 0 1 3 4a1 1 0 0 1 1-1h3.5a1 1 0 0 1 1 1c0 1.25.2 2.45.57 3.57a1 1 0 0 1-.25 1z" fill="var(--red)"/></svg>
        8347 2516
      </div>
      <span class="hours-pill">24 Hour Business 7 Days</span>
    </div>

    <h2 class="services-title">Our Service</h2>

    <ul class="service-list list-left">
      <li><svg viewBox="0 0 16 16"><rect x="2" y="2" width="12" height="12" rx="3" fill="none" stroke="#fff" stroke-width="1.5"/></svg>Towing</li>
      <li><svg viewBox="0 0 16 16"><rect x="2" y="2" width="12" height="12" rx="3" fill="none" stroke="#fff" stroke-width="1.5"/></svg>Accident Towing</li>
      <li><svg viewBox="0 0 16 16"><rect x="2" y="2" width="12" height="12" rx="3" fill="none" stroke="#fff" stroke-width="1.5"/></svg>Mechanical Breakdown</li>
    </ul>

    <ul class="service-list list-right">
      <li><svg viewBox="0 0 16 16"><rect x="2" y="2" width="12" height="12" rx="3" fill="none" stroke="#fff" stroke-width="1.5"/></svg>4WD Off Road Towing</li>
      <li><svg viewBox="0 0 16 16"><rect x="2" y="2" width="12" height="12" rx="3" fill="none" stroke="#fff" stroke-width="1.5"/></svg>Light &amp; Heavy Towing</li>
      <li><svg viewBox="0 0 16 16"><path d="M8 1.5 14 4v4c0 3.5-2.6 5.8-6 6.8C4.6 13.8 2 11.5 2 8V4z" fill="none" stroke="#fff" stroke-width="1.4"/><path d="M5.5 8l2 2 3-3.5" fill="none" stroke="#fff" stroke-width="1.4"/></svg>Insurance, Salvage &amp; Recovery</li>
    </ul>
  </section>
</main>
</body>
</html>
```